Mental Health Services for Employees - we need a website for our new business

We need a simple web design to showcase our various services. Our programs help organizations to ensure the heath and wellness of their workers. Our company is called "Brightway Workplace Partners Inc." or "Brightway" We'd like to see designs that use the colour palette from our logo. Our customers our fairly conservative, and our design should communicate due diligence around providing a safe and healthy environment for workers. Attached our the logo files. Also sample photographs from our purchased images - others available. Original design for website is found here: https://lanternow7.examplesite.com/mypage-1 A key page not listed in our original design is a section that lists "Five Reasons to Work With Us". We will need to be able to modify and change the copy/menu options as the business grows.

Target Market(s)

businesses who want to provide health and wellness services for their employees

Coding

Coded - Design and coding required

Number of Pages Required

2 page

Font styles to use
Sans Serif

Requirements
Must have
• colours that work with our attached logo

```html
<!DOCTYPE html>
<html lang="en">
<head>
<meta charset="utf-8">
<title>Brightway Workplace Partners</title>
<link href="https://fonts.googleapis.com/css2?family=Montserrat:ital,wght@0,400;0,500;0,600;0,700;1,400&display=swap" rel="stylesheet">
<style>
:root{
  --teal:#19a59b;
  --yellow:#f4b41a;
  --ink:#1d1d1d;
  --text:#555;
  --muted:#8a8a8a;
  --dark:#121212;
  --paper:#fff;
  --light:#f4f4f4;
}
*{box-sizing:border-box;margin:0;padding:0}
html,body{width:1200px;height:3805px;overflow:hidden;background:var(--paper)}
body{font-family:"Montserrat",sans-serif;color:var(--text);position:relative}
.abs{position:absolute}
.page{position:relative;width:1200px;height:3805px;overflow:hidden}

/* header */
.header{left:0;top:0;width:1200px;height:96px;background:var(--paper);z-index:5}
.brand{left:89px;top:22px;display:flex;align-items:center;gap:10px}
.brand-mark{width:22px;height:22px;background:var(--teal);border-radius:50%}
.brand-name{font-weight:700;font-size:18px;color:var(--ink);line-height:1.05}
.brand-name small{display:block;font-size:11px;font-weight:700;color:var(--ink);letter-spacing:.3px}
.nav{left:393px;top:38px;display:flex;gap:22px;font-size:11px;font-weight:600;color:var(--ink)}
.nav .active{color:var(--teal);border-bottom:2px solid var(--teal);padding-bottom:4px}
.call{left:807px;top:36px;font-size:15px;font-weight:700;color:var(--teal)}
.btn-solid{background:var(--teal);color:#fff;font-size:11px;font-weight:600;text-align:center;letter-spacing:.5px}
.quote-btn{left:984px;top:31px;width:127px;height:32px;line-height:32px}

/* hero */
.hero-photo{left:0;top:96px;width:1200px;height:560px;background:linear-gradient(100deg,#5b5a55 0%,#8b8577 35%,#c86a2b 62%,#d97a30 75%,#b6b0a5 100%)}
.hero-shade{left:0;top:96px;width:1200px;height:560px;background:linear-gradient(90deg,rgba(0,0,0,.55),rgba(0,0,0,.05) 60%)}
.hero-title{left:89px;top:276px;font-size:25px;font-weight:600;color:#fff;line-height:1.45}
.hero-sub{left:89px;top:358px;font-size:17px;font-weight:500;color:#fff}
.btn-outline{border:1px solid #fff;color:#fff;font-size:11px;font-weight:600;text-align:center;letter-spacing:.5px}
.hero-btn{left:89px;top:418px;width:127px;height:32px;line-height:30px}
.dots-v{left:1094px;top:253px;display:flex;flex-direction:column;gap:9px}
.dots-v i{width:12px;height:12px;border:1px solid #fff;border-radius:50%;display:block}
.dots-v i.on{background:#fff}

/* section headings */
.eyebrow{left:0;width:1200px;text-align:center;font-size:11px;font-weight:600;color:var(--teal);letter-spacing:1px}
.eyebrow span{position:relative;padding:0 12px}
.eyebrow span:before{content:"";position:absolute;right:100%;top:50%;width:60px;height:1px;background:var(--teal)}
.h2{left:0;width:1200px;text-align:center;font-size:24px;font-weight:600;color:var(--ink);letter-spacing:.5px}

/* services */
.svc-photo{top:743px;width:319px;height:196px}
.svc-card{top:875px;width:256px;height:280px;background:#fff;box-shadow:0 8px 24px rgba(0,0,0,.12);text-align:center;padding:70px 22px 0}
.svc-card:before{content:"";position:absolute;left:0;top:-18px;width:256px;height:24px;background:linear-gradient(172deg,transparent 49%,var(--yellow) 50%)}
.svc-card h3{font-size:17px;font-weight:600;color:var(--ink);line-height:1.15;margin-bottom:18px}
.svc-card p{font-size:12.5px;line-height:1.55;color:var(--muted)}
.svc-card .more{display:inline-block;margin-top:26px;font-size:11px;font-weight:700;color:var(--ink);border-bottom:2px solid var(--ink);padding-bottom:2px}
.svc-card .more.teal{color:var(--teal);border-color:var(--teal)}

/* about */
.about-photo{left:0;top:1230px;width:1200px;height:560px;background:linear-gradient(180deg,#2a2a28 0%,#3c3a33 45%,#1a1a18 100%)}
.about-text{left:260px;top:1506px;width:680px;text-align:center;color:#eee;font-size:12.5px;line-height:1.6}
.about-text p+p{margin-top:16px}
.about-btn{left:528px;top:1654px;width:144px;height:32px;line-height:30px;border:1px solid var(--teal);color:#eee;font-size:11px;font-weight:600;text-align:center}

/* reasons */
.reasons-photo{left:89px;top:1936px;width:447px;height:360px;background:linear-gradient(135deg,#9aa3aa 0%,#5e6a73 40%,#d59a2c 70%,#e3b04a 100%)}
.reasons-eyebrow{left:617px;top:1928px;font-size:11px;font-weight:600;color:var(--teal);letter-spacing:1px}
.reasons-eyebrow:after{content:"";display:inline-block;width:60px;height:1px;background:var(--teal);vertical-align:middle;margin-left:12px}
.reasons-title{left:617px;top:1958px;font-size:24px;font-weight:600;color:var(--ink)}
.reasons-list{left:617px;top:2018px;width:500px;list-style:none}
.reasons-list li{position:relative;padding-left:36px;font-size:14px;line-height:1.5;color:var(--text);margin-bottom:14px}
.reasons-list li:before{content:"";position:absolute;left:0;top:3px;width:14px;height:14px;border:1.5px solid var(--yellow)}
.reasons-list li:after{content:"";position:absolute;left:4px;top:6px;width:5px;height:3px;border-left:1.5px solid var(--yellow);border-bottom:1.5px solid var(--yellow);transform:rotate(-45deg)}
.reasons-btn{left:617px;top:2268px;width:127px;height:32px;line-height:32px}

/* testimonials */
.testi-photo{left:0;top:2360px;width:1200px;height:620px;background:linear-gradient(90deg,#e8ddd6 0%,#f1ece8 40%,#ece6e1 70%,#dcd3cc 100%)}
.testi-veil{left:0;top:2360px;width:1200px;height:620px;background:rgba(255,255,255,.72)}
.quote-mark{left:0;width:1200px;top:2586px;text-align:center;font-size:44px;font-weight:700;color:var(--yellow);line-height:1}
.testi-text{left:270px;top:2648px;width:660px;text-align:center;font-size:14px;font-style:italic;line-height:1.55;color:var(--ink)}
.testi-name{left:0;width:1200px;top:2752px;text-align:center;font-size:11px;font-weight:700;color:var(--teal)}
.dots-h{left:561px;top:2806px;display:flex;gap:9px}
.dots-h i{width:12px;height:12px;border:1.5px solid #444;border-radius:50%;display:block}
.dots-h i.on{border-color:var(--teal);background:radial-gradient(var(--teal) 35%,transparent 40%)}

/* form */
.field{top:3095px;height:32px;border:1px solid #ddd;background:#fafafa;font-size:10px;color:#888;padding:10px 14px;font-weight:500}
.field.msg{left:208px;top:3141px;width:782px;height:107px}
.send{left:535px;top:3268px;width:127px;height:31px;line-height:29px;border:1px solid var(--teal);color:var(--teal);font-size:11px;font-weight:600;text-align:center}

/* footer */
.footer{left:0;top:3462px;width:1200px;height:343px;background:var(--dark)}
.foot-brand{left:89px;top:3530px;text-align:left}
.foot-mark{width:36px;height:36px;background:#fff;border-radius:50%;margin:0 0 14px 34px}
.foot-name{font-size:22px;font-weight:700;color:#fff;line-height:1.1}
.foot-name small{display:block;font-size:13px;font-weight:600;color:#fff}
.foot-h{font-size:15px;font-weight:700;color:var(--yellow)}
.foot-links{list-style:none;font-size:11.5px;color:#aaa;line-height:2.05}
.foot-contact{font-size:11.5px;color:#aaa;line-height:1.7}
.foot-contact b{color:var(--teal);font-size:14px}
.social{display:flex;gap:12px}
.social i{width:30px;height:30px;border-radius:50%;background:#666;display:block}
.social i.on{background:var(--teal)}
.to-top{left:1100px;top:3512px}
.foot-rule{left:89px;top:3736px;width:1022px;height:1px;background:#2c2c2c}
.copyright{left:0;top:3760px;width:1200px;text-align:center;font-size:11px;color:#999}
.copyright span{color:var(--yellow)}
</style>
</head>
<body>
<div class="page">

  <!-- header -->
  <header class="abs header">
    <div class="abs brand"><span class="brand-mark"></span><div class="brand-name">BRIGHTWAY<small>Workplace Partners</small></div></div>
    <nav class="abs nav"><span class="active">HOME</span><span>ABOUT US</span><span>SERVICES</span><span>SAP</span><span>CONTACT US</span></nav>
    <div class="abs call">Call: 555-204-7781</div>
    <div class="abs btn-solid quote-btn">GET A QUOTE</div>
  </header>

  <!-- hero -->
  <div class="abs hero-photo" role="img" aria-label="Smiling site worker in an orange safety jacket and yellow hard hat beside heavy machinery"></div>
  <div class="abs hero-shade"></div>
  <svg class="abs" style="left:0;top:480px" width="1200" height="180" viewBox="0 0 1200 180">
    <polygon points="0,176 1200,92 1200,180 0,180" fill="#fff"/>
    <polygon points="700,126 1200,16 1200,92" fill="var(--yellow)"/>
  </svg>
  <h1 class="abs hero-title">WE PROMOTE HEALTH, WELLNESS, AND<br>SAFETY IN THE WORKPLACE!</h1>
  <div class="abs hero-sub">We are here to help you ...</div>
  <div class="abs btn-outline hero-btn">CONTACT US</div>
  <div class="abs dots-v"><i></i><i class="on"></i><i></i><i></i></div>

  <!-- services -->
  <div class="abs eyebrow" style="top:654px"><span>WHAT WE DO</span></div>
  <h2 class="abs h2" style="top:680px">SERVICES WE PROVIDE</h2>

  <div class="abs svc-photo" style="left:89px;background:linear-gradient(135deg,#5b6b3c,#a9b07a 50%,#c8482c)" role="img" aria-label="Forestry worker in protective gear cutting a tree with a chainsaw"></div>
  <div class="abs svc-photo" style="left:440px;background:linear-gradient(135deg,#cfd3d6,#8f7a6a 50%,#e9e6e2)" role="img" aria-label="Friendly support agent wearing a headset at a desk"></div>
  <div class="abs svc-photo" style="left:792px;background:linear-gradient(135deg,#d9d3cb,#7a5e4c 50%,#c7bdb2)" role="img" aria-label="Counsellor listening to a client in a calm office"></div>

  <div class="abs svc-card" style="left:119px">
    <h3>Accommodation<br>Screening</h3>
    <p>For customers who primarily want an opinion whether they are obliged to provide accommodation ...</p>
    <span class="more">READ MORE</span>
  </div>
  <div class="abs svc-card" style="left:470px;top:860px;box-shadow:0 14px 34px rgba(0,0,0,.18)">
    <h3>SAP<br>Assessments</h3>
    <p>The team at Brightway assists in analyzing an organization's Alcohol and Drug Policy and taking ...</p>
    <span class="more teal">READ MORE</span>
  </div>
  <div class="abs svc-card" style="left:822px">
    <h3>Specialized Addiction<br>Case Management</h3>
    <p>This is a unique and specialized program offered by Brightway that focuses on the needs of individuals struggling ...</p>
    <span class="more">READ MORE</span>
  </div>

  <!-- about -->
  <div class="abs about-photo" role="img" aria-label="Large mining haul trucks at dusk, darkened"></div>
  <svg class="abs" style="left:0;top:1220px" width="1200" height="580" viewBox="0 0 1200 580">
    <polygon points="0,86 1200,8 1200,0 0,0" fill="#fff"/>
    <polygon points="0,86 1200,8 1200,48 0,152" fill="rgba(18,18,18,.55)"/>
    <polygon points="0,86 700,40 0,152" fill="var(--teal)"/>
    <polygon points="0,580 1200,480 1200,580" fill="#fff"/>
    <polygon points="560,527 1200,430 1200,480" fill="var(--yellow)"/>
  </svg>
  <div class="abs eyebrow" style="top:1396px;color:var(--teal)"><span>ABOUT US</span></div>
  <h2 class="abs h2" style="top:1424px;color:#fff;line-height:1.3">WE PROMOTE HEALTH, WELLNESS, AND SAFETY<br>IN THE WORKPLACE!</h2>
  <div class="abs about-text">
    <p>Brightway Workplace Partners Inc. ("Brightway") provides outstanding business-to-business services that support and promote health, wellness, and safety in the workplace. Brightway's flagship programs are the Substance Abuse Professional (SAP) and Specialized Addiction Case Management services.</p>
    <p>Brightway is ready to provide organizations with access to a suite of best-practice solutions and options for your employees ...</p>
  </div>
  <div class="abs about-btn">DISCOVER MORE</div>

  <!-- reasons -->
  <div class="abs reasons-photo" role="img" aria-label="Worker in a safety harness clipping a hook onto a yellow rail"></div>
  <div class="abs reasons-eyebrow">WHY BRIGHTWAY</div>
  <h2 class="abs reasons-title">FIVE REASONS TO WORK WITH US</h2>
  <ul class="abs reasons-list">
    <li>Contrary to popular belief, Lorem Ipsum is not simply random text. It has roots in a piece.</li>
    <li>There are many variations of passages of Lorem Ipsum.</li>
    <li>Contrary to popular belief, Lorem Ipsum is not simply random.</li>
    <li>Contrary to popular belief, Lorem Ipsum is not simply random text. It has roots in a piece.</li>
    <li>There are many variations of passages of Lorem Ipsum.</li>
  </ul>
  <div class="abs btn-solid reasons-btn">CONTACT US</div>

  <!-- testimonials -->
  <div class="abs testi-photo" role="img" aria-label="Happy family group together outdoors, softly faded"></div>
  <div class="abs testi-veil"></div>
  <svg class="abs" style="left:0;top:2350px" width="1200" height="640" viewBox="0 0 1200 640">
    <polygon points="0,0 1200,0 1200,10 0,70" fill="#fff"/>
    <polygon points="0,70 1200,10 1200,0 860,0 0,130" fill="var(--teal)" opacity="0"/>
    <polygon points="0,70 560,42 0,130" fill="var(--teal)"/>
    <polygon points="0,640 1200,560 1200,640" fill="#fff"/>
    <polygon points="600,600 1200,488 1200,560" fill="var(--yellow)"/>
  </svg>
  <div class="abs eyebrow" style="top:2511px"><span>TESTIMONIALS</span></div>
  <h2 class="abs h2" style="top:2537px">WHAT PEOPLE SAY</h2>
  <div class="abs quote-mark">&#8220;&#8220;</div>
  <p class="abs testi-text">There are many variations of passages of Lorem Ipsum available, but the majority have suffered alteration in some form, by injected humour, or randomised words which don't look even slightly believable. If you are going to use a passage of Lorem Ipsum, you need to be sure there isn't anything embarrassing hidden in the ...</p>
  <div class="abs testi-name">STANDARD CHUNK</div>
  <div class="abs dots-h"><i></i><i class="on"></i><i></i><i></i></div>

  <!-- quote form -->
  <div class="abs eyebrow" style="top:3005px"><span>GET A QUOTE</span></div>
  <h2 class="abs h2" style="top:3032px">SEND US A MESSAGE</h2>
  <div class="abs field" style="left:208px;width:252px">NAME</div>
  <div class="abs field" style="left:473px;width:252px">EMAIL</div>
  <div class="abs field" style="left:738px;width:252px">PHONE</div>
  <div class="abs field msg">TYPE YOUR MESSAGE ...</div>
  <div class="abs send">SEND</div>

  <!-- footer -->
  <svg class="abs" style="left:0;top:3380px" width="1200" height="90" viewBox="0 0 1200 90">
    <polygon points="0,8 1200,62 1200,84 0,84" fill="var(--dark)"/>
    <polygon points="0,8 620,36 0,84" fill="var(--teal)"/>
  </svg>
  <footer class="abs footer"></footer>
  <div class="abs foot-brand"><div class="foot-mark"></div><div class="foot-name">BRIGHTWAY<small>Workplace Partners</small></div></div>

  <div class="abs foot-h" style="left:375px;top:3512px">Quick Links</div>
  <ul class="abs foot-links" style="left:375px;top:3544px">
    <li>About Us</li><li>Services</li><li>SAP</li><li>Blog</li><li>Testimonials</li><li>Contact Us</li>
  </ul>

  <div class="abs foot-h" style="left:584px;top:3512px">Contact Us</div>
  <div class="abs foot-contact" style="left:584px;top:3544px">
    <b>Call: 555-204-7781</b><br>E: hello@brightway-wp.com<br><br>Fax: 555-204-7790<br><br>118 Harbour Lane, Suite 210<br>Lakeview ON K0L 2B0
  </div>

  <div class="abs foot-h" style="left:880px;top:3512px">Follow Us</div>
  <div class="abs social" style="left:880px;top:3552px"><i></i><i class="on"></i><i></i></div>

  <svg class="abs to-top" width="22" height="22" viewBox="0 0 22 22"><path d="M4 18 L11 4 L18 18 M7 12 H15" stroke="var(--teal)" stroke-width="2" fill="none"/></svg>
  <div class="abs foot-rule"></div>
  <div class="abs copyright">© 2019 <span>Brightway Workplace Partners Inc.</span> All Right Reserved</div>
</div>
</body>
</html>
```